Healthcare IT company looking for business card design

We develop IT systems for healthcare that significantly reduces cost and improves quality.

We want a business card design that is professional and clean, and using the colors in our logo.

Target Market(s)

Doctors and decision makers in the healthcare industry

Industry/Entity Type

Healthcare

Contact Information for Business Card

It should include
Name and title, address, telephone

Tobias Vrenholt, CEO
+46 712 418257
tobias@kelvaro.se

Font styles to use
Serif

Colors
0355a3
ed282f

Requirements
Must have
• Clean design
• Professional feel
Nice to have
• N/A
Should not have
• N/A

```html
<!DOCTYPE html>
<html lang="en">
<head>
<meta charset="utf-8">
<title>Kelvaro business cards</title>
<link rel="stylesheet" href="https://fonts.googleapis.com/css2?family=Open+Sans:wght@400;600;700&display=swap">
<style>
  :root {
    --brand-blue: #0355a3;
    --card-blue: #0a5bab;
    --map-blue: #1363b1;
    --brand-red: #ed282f;
    --paper: #ffffff;
    --ink: #333333;
    --backdrop: #8c8c8c;
    --divider: #cfcfcf;
  }
  * { margin: 0; padding: 0; box-sizing: border-box; }
  html, body { width: 1200px; height: 828px; overflow: hidden; }
  body {
    background: var(--backdrop);
    font-family: "Open Sans", Arial, sans-serif;
    position: relative;
  }
  .card { position: absolute; overflow: hidden; }

  /* Front card */
  .card-front {
    left: 324px; top: 62px; width: 536px; height: 305px;
    background: var(--paper);
  }
  .wordmark {
    position: absolute; font-weight: 700; letter-spacing: -1px; line-height: 1;
  }
  .card-front .wordmark {
    left: 40px; top: 128px; font-size: 58px; color: var(--brand-blue);
  }
  .front-divider {
    position: absolute; left: 268px; top: 78px; width: 1px; height: 152px;
    background: var(--divider);
  }
  .holder-name {
    position: absolute; left: 287px; top: 70px;
    font-size: 17px; font-weight: 700; color: var(--brand-blue); letter-spacing: 0.3px;
  }
  .holder-title {
    position: absolute; left: 287px; top: 91px;
    font-size: 16px; color: var(--brand-red);
  }
  .address {
    position: absolute; left: 287px; top: 123px;
    font-size: 13px; line-height: 20px; color: var(--ink);
  }
  .contact-list {
    position: absolute; left: 288px; top: 175px; list-style: none;
    font-size: 13px; color: var(--ink);
  }
  .contact-list li { display: flex; align-items: center; height: 20px; }
  .contact-list svg { width: 13px; height: 13px; margin-right: 10px; fill: var(--brand-blue); }
  .stripe-red {
    position: absolute; left: 0; top: 288px; width: 100%; height: 3px; background: var(--brand-red);
  }
  .stripe-blue {
    position: absolute; left: 0; top: 293px; width: 100%; height: 12px; background: var(--brand-blue);
  }

  /* Back cards */
  .card-back { background: var(--card-blue); }
  .card-back-feature { left: 52px; top: 432px; width: 530px; height: 303px; }
  .card-back-centered { left: 628px; top: 431px; width: 533px; height: 304px; }
  .world-map {
    position: absolute; left: 10px; top: 20px; width: 510px; height: 250px;
    background: radial-gradient(ellipse at center, var(--map-blue) 0%, var(--card-blue) 75%);
  }
  .card-back .wordmark { color: var(--paper); }
  .card-back-feature .wordmark { left: 128px; top: 196px; font-size: 62px; }
  .brand-square {
    position: absolute; left: 354px; top: 150px; width: 110px; height: 110px;
    background: var(--brand-red); border-radius: 6px;
  }
  .card-back-centered .wordmark { left: 0; width: 100%; text-align: center; top: 128px; font-size: 58px; }
  .web {
    position: absolute; color: var(--paper); font-size: 16px; letter-spacing: 1px;
  }
  .card-back-feature .web { left: 168px; top: 258px; }
  .card-back-centered .web { left: 0; width: 100%; text-align: center; top: 268px; }
</style>
</head>
<body>

<section class="card card-front">
  <div class="wordmark">Kelvaro</div>
  <div class="front-divider"></div>
  <div class="holder-name">Tobias Vrenholt</div>
  <div class="holder-title">Ceo</div>
  <div class="address">Street Name, City Name,<br>Zip Code - 00000</div>
  <ul class="contact-list">
    <li>
      <svg viewBox="0 0 16 16"><path d="M3 2h3l1.5 3.5-2 1.2a8 8 0 0 0 3.8 3.8l1.2-2L14 10v3a1.5 1.5 0 0 1-1.5 1.5A11.5 11.5 0 0 1 1.5 3.5 1.5 1.5 0 0 1 3 2z"/></svg>
      +46 712 418257
    </li>
    <li>
      <svg viewBox="0 0 16 16"><path d="M1 4h14v9H1z M1 4l7 5 7-5" fill="none" stroke="#0355a3" stroke-width="1.6"/></svg>
      tobias@kelvaro.se
    </li>
    <li>
      <svg viewBox="0 0 16 16"><circle cx="8" cy="8" r="6.5" fill="none" stroke="#0355a3" stroke-width="1.4"/><path d="M1.5 8h13M8 1.5c-3 3.5-3 9.5 0 13M8 1.5c3 3.5 3 9.5 0 13" fill="none" stroke="#0355a3" stroke-width="1.1"/></svg>
      www.kelvaro.se
    </li>
  </ul>
  <div class="stripe-red"></div>
  <div class="stripe-blue"></div>
</section>

<section class="card card-back card-back-feature">
  <div class="world-map" role="img" aria-label="Faint dotted world map in lighter blue"></div>
  <div class="brand-square"></div>
  <div class="wordmark">Kelvaro</div>
  <div class="web">www.kelvaro.se</div>
</section>

<section class="card card-back card-back-centered">
  <div class="world-map" role="img" aria-label="Faint dotted world map in lighter blue"></div>
  <div class="wordmark">Kelvaro</div>
  <div class="web">www.kelvaro.se</div>
</section>

</body>
</html>
```